Award-winnning Estate Agent needs a premium version of their 'For Sale' board design

We need a premium option for our 'For Sale' board design. We have a standard board that is attached to this brief, but were are looking to have a premium design version that we will use when selling exclusive properties. Our company name is Harbour Lane Estates and the name for this is exclusive selection is: 'The Harbour Collection'. The design needs to work with our current brand, but have a distinctive PREMIUM feel to it. I have uploaded the barnd guidelines and also some of the exisisting logo variations. We do NOT need a new logo but feel free to play around with colours, fonts, sizes etc. for the sign.

Target Market(s)

Property buyers & house hunters

Industry/Entity Type

Real Estate - Residential Property

Font styles to use
Sans Serif

Requirements
Must have
• A premium fee, must be square design, must be easy to read when driving past the sign
Nice to have
• I'm open ot ideas

```html
<!DOCTYPE html>
<html lang="en">
<head>
<meta charset="utf-8">
<title>Harbour Lane Estates – For Sale Boards</title>
<link href="https://fonts.googleapis.com/css2?family=Inter:wght@300;400&display=swap" rel="stylesheet">
<style>
  :root {
    --backdrop: #d9dadc;
    --navy: #0f3282;
    --sky: #3aa8dc;
    --white: #ffffff;
  }
  * { margin: 0; padding: 0; box-sizing: border-box; }
  html, body {
    width: 1200px; height: 900px; overflow: hidden;
    background: var(--backdrop);
    font-family: "Inter", Arial, sans-serif;
  }
  .canvas { position: relative; width: 1200px; height: 900px; }

  .board {
    position: absolute; top: 282px;
    width: 336px; height: 336px;
    background: var(--navy); color: var(--white);
    overflow: hidden;
  }
  .board--left { left: 86px; }
  .board--centre { left: 433px; }
  .board--light { left: 780px; background: var(--white); color: var(--navy); }

  .board > * { position: absolute; white-space: nowrap; }

  .brand-mark {
    width: 34px; height: 34px; top: 42px;
    background: var(--sky);
  }
  .brand-name {
    top: 102px; font-size: 19px; font-weight: 400;
    color: var(--sky); letter-spacing: -0.1px;
  }
  .board--light .brand-name { color: var(--navy); }

  .headline {
    top: 134px; font-size: 80px; font-weight: 300;
    line-height: 1; letter-spacing: -1px;
  }
  .collection {
    top: 222px; font-size: 16.5px; font-weight: 300;
    color: var(--sky); letter-spacing: 0.2px;
  }
  .phone {
    top: 262px; font-size: 31px; font-weight: 300;
    line-height: 1; letter-spacing: 0.3px;
  }
  .web {
    top: 304px; font-size: 14px; font-weight: 400;
    letter-spacing: 0.2px;
  }

  /* left-aligned board */
  .board--left .brand-mark { left: 35px; }
  .board--left .brand-name,
  .board--left .headline,
  .board--left .collection,
  .board--left .phone,
  .board--left .web { left: 33px; }
  .board--left .collection { left: 35px; }
  .rule {
    left: 33px; top: 296px; width: 268px; height: 2px;
    background: var(--sky);
  }

  /* centred boards */
  .board--centre .brand-mark,
  .board--light .brand-mark { left: 151px; }
  .board--centre .brand-name,
  .board--centre .headline,
  .board--centre .collection,
  .board--centre .phone,
  .board--centre .web,
  .board--light .brand-name,
  .board--light .headline,
  .board--light .collection { left: 0; width: 336px; text-align: center; }
  .board--centre .web { top: 306px; font-size: 13px; }

  /* light board bands */
  .phone-band {
    left: 0; top: 259px; width: 244px; height: 34px;
    background: var(--sky);
  }
  .board--light .phone {
    left: 26px; top: 262px; color: var(--white);
  }
  .web-band {
    left: 58px; top: 292px; width: 278px; height: 24px;
    background: var(--navy);
  }
  .board--light .web {
    left: 58px; top: 296px; width: 278px; text-align: center;
    font-size: 13px; color: var(--white);
  }
</style>
</head>
<body>
<main class="canvas">

  <section class="board board--left" aria-label="For Sale board, dark, left aligned">
    <span class="brand-mark" aria-hidden="true"></span>
    <p class="brand-name">Harbour Lane Estates</p>
    <h2 class="headline">For Sale</h2>
    <p class="collection">THE HARBOUR COLLECTION</p>
    <p class="phone">01632 960418</p>
    <span class="rule" aria-hidden="true"></span>
    <p class="web">www.harbourlaneestates.co.uk</p>
  </section>

  <section class="board board--centre" aria-label="For Sale board, dark, centred">
    <span class="brand-mark" aria-hidden="true"></span>
    <p class="brand-name">Harbour Lane Estates</p>
    <h2 class="headline">For Sale</h2>
    <p class="collection">THE HARBOUR COLLECTION</p>
    <p class="phone">01632 960418</p>
    <p class="web">www.harbourlaneestates.co.uk</p>
  </section>

  <section class="board board--light" aria-label="For Sale board, white">
    <span class="brand-mark" aria-hidden="true"></span>
    <p class="brand-name">Harbour Lane Estates</p>
    <h2 class="headline">For Sale</h2>
    <p class="collection">THE HARBOUR COLLECTION</p>
    <span class="phone-band" aria-hidden="true"></span>
    <p class="phone">01632 960418</p>
    <span class="web-band" aria-hidden="true"></span>
    <p class="web">www.harbourlaneestates.co.uk</p>
  </section>

</main>
</body>
</html>
```